Construction company looking for modern

**Tallow Crest Joinery Limited**

We need a website for a renovation/remodeling company based in Hamilton, New Zealand. Ideally it will catch clients' attention and be modern and professional looking. I have attached a logo that I have just recently had made (through PixelHarbor). If the website could reflect this style and colour schemes, that would be awesome. The final design should communicate a trustworthiness and professionalism.

I have attached photos of a website that I really think is great, so if we could have something that follows along those likes,

https://www.dailyplover.example/local-news/news/local-builder-named-top-apprentice-for-region/QZTRPLA8VXN2MJ5DFYUEKHSWGO/

I won a competition a few years ago while I was an apprentice, If we could somehow put that in there as one of my achievements to try to bring in some trust that would be awesome. I would like to add a new picture though because my beard in that photo is wild.

Target Market(s)

Families that want live in the homes that i'm working on. not investors. People that are looking for quality not cheapest price.

Industry/Entity Type

Construction, Home renovations, Maintenance, Deck Builds, New Builds, Bathrooms, Kitchens

Coding

Coded - Design and coding required

Number of Pages Required

5+ page

Font styles to use
Sans Serif

Colors
6B429C
8869AF
B7A5CE
E3DAEB
F3F0F8

Requirements
Must have
• Contact us page, large clear pictures, Colours the work with the purple in my logo. That will be my company colour so I'm thinking black and purple, or what ever compliments purple nicely
Nice to have
• Page for Renovations, Testimonials, Contact us, Home, About us
Should not have
• Plain looking pages, empty white space, I want the text to be beside a nice big picture etc

```html
<!DOCTYPE html>
<html lang="en">
<head>
<meta charset="utf-8">
<title>Tallow Crest Joinery — Menu</title>
<link href="https://fonts.googleapis.com/css2?family=Outfit:wght@400;500;700&display=swap" rel="stylesheet">
<style>
  :root {
    --purple: #6b429c;
    --purple-deep: #4b2a72;
    --lilac: #b7a5ce;
    --mist: #e3daeb;
    --white: #ffffff;
    --ink: #2b2b2b;
    --hero-text: rgba(200, 200, 200, 0.62);
    --tab-bg: rgba(243, 240, 248, 0.72);
  }
  * { margin: 0; padding: 0; box-sizing: border-box; }
  html, body { width: 1200px; height: 675px; overflow: hidden; }
  body { position: relative; font-family: "Outfit", sans-serif; background: #555; }

  .hero-photo {
    position: absolute; inset: 0 406px 0 0;
    background:
      linear-gradient(rgba(30,30,30,0.45), rgba(30,30,30,0.45)),
      radial-gradient(ellipse at 60% 35%, #e8e8e8 0%, #bdbdbd 45%, #8e8e8e 100%);
  }
  .hero-rug {
    position: absolute; left: 90px; right: 430px; top: 470px; height: 170px;
    background: linear-gradient(#7d7d7d, #6a6a6a);
    opacity: 0.35;
  }
  .brand {
    position: absolute; left: 0; top: 0; width: 125px; height: 75px;
    background: var(--white);
    display: flex; align-items: center; justify-content: center; gap: 5px;
  }
  .brand-mark { width: 9px; height: 9px; background: var(--purple); border-radius: 50%; }
  .brand-name { font-weight: 700; font-size: 10px; line-height: 1.15; color: var(--purple); width: 82px; }

  .hero-title {
    position: absolute; left: 200px; top: 220px; width: 580px;
    font-weight: 700; font-size: 44px; line-height: 54px; letter-spacing: 1px;
    color: var(--hero-text);
  }
  .hero-cta {
    position: absolute; left: 200px; top: 411px; width: 112px; height: 38px;
    background: var(--purple-deep); color: var(--lilac);
    font-size: 11px; font-weight: 500;
    display: flex; align-items: center; justify-content: center;
  }
  .side-tab {
    position: absolute; left: 0; top: 275px; width: 31px; height: 125px;
    background: var(--tab-bg); border-radius: 0 10px 10px 0;
    display: flex; align-items: center; justify-content: center;
  }
  .side-tab span { transform: rotate(-90deg); white-space: nowrap; font-size: 11px; color: var(--purple); }
  .bottom-tab {
    position: absolute; left: 537px; top: 644px; width: 125px; height: 31px;
    background: var(--tab-bg); border-radius: 10px 10px 0 0;
    display: flex; align-items: center; justify-content: center;
    font-size: 11px; color: var(--purple); font-weight: 500;
  }

  .menu-panel {
    position: absolute; left: 794px; top: 0; width: 406px; height: 675px;
    background: var(--purple);
  }
  .menu-close {
    position: absolute; right: 0; top: 0; width: 75px; height: 75px;
    background: var(--white); display: flex; align-items: center; justify-content: center;
  }
  .menu-nav { position: absolute; left: 62px; top: 78px; list-style: none; }
  .menu-nav li { height: 50px; font-size: 25px; font-weight: 700; color: var(--white); line-height: 36px; }
  .menu-nav li.is-active span { color: var(--lilac); text-decoration: underline; text-decoration-thickness: 1px; text-underline-offset: 3px; }

  .contact-list { position: absolute; left: 62px; top: 347px; list-style: none; }
  .contact-item { display: flex; align-items: flex-start; gap: 13px; margin-bottom: 6px; }
  .contact-icon { width: 44px; height: 44px; flex: none; }
  .contact-text { font-size: 14px; color: var(--white); line-height: 19px; padding-top: 12px; }

  .social-list { position: absolute; left: 62px; top: 559px; display: flex; gap: 6px; }
  .social-dot { width: 31px; height: 31px; border-radius: 50%; background: #2a2a2a; }
  .social-dot.is-hover { background: var(--white); }
</style>
</head>
<body>
  <div class="hero-photo" role="img" aria-label="Bright living room interior with grey sofa, yellow cushions, pendant lamps and patterned rug, dimmed behind the open menu"></div>
  <div class="hero-rug" aria-hidden="true"></div>

  <div class="brand">
    <span class="brand-mark"></span>
    <span class="brand-name">Tallow Crest Joinery</span>
  </div>

  <h1 class="hero-title">We’re an independent family-owned, new home building company</h1>
  <div class="hero-cta">Contact Us</div>

  <div class="side-tab"><span>About Us</span></div>
  <div class="bottom-tab">Renovations</div>

  <aside class="menu-panel">
    <ul class="menu-nav">
      <li>Home</li>
      <li>About Us</li>
      <li class="is-active"><span>Renovations</span></li>
      <li>Testimonials</li>
      <li>Contact Us</li>
    </ul>

    <ul class="contact-list">
      <li class="contact-item">
        <svg class="contact-icon" viewBox="0 0 44 44"><path d="M22 1 L43 22 L22 43 L1 22 Z" fill="none" stroke="#fff" stroke-width="1"/><path d="M17 17 q1-1 2 0 l1.5 2 q.5 1-.5 1.5 q1 2.5 3.5 3.5 q.5-1 1.5-.5 l2 1.5 q1 1 0 2 q-1.5 1.5-3.5.5 q-5-2.5-7-7 q-1-2 .5-3.5 Z" fill="#fff"/></svg>
        <span class="contact-text">(555) 014-2287</span>
      </li>
      <li class="contact-item">
        <svg class="contact-icon" viewBox="0 0 44 44"><path d="M22 1 L43 22 L22 43 L1 22 Z" fill="none" stroke="#fff" stroke-width="1"/><path d="M16.5 20 L22 16 L27.5 20 V27 H16.5 Z" fill="#fff"/><path d="M16.5 20 L22 24 L27.5 20" fill="none" stroke="#6b429c" stroke-width="1"/></svg>
        <span class="contact-text">info@tallowcrestjoinery.com</span>
      </li>
      <li class="contact-item">
        <svg class="contact-icon" viewBox="0 0 44 44"><path d="M22 1 L43 22 L22 43 L1 22 Z" fill="none" stroke="#fff" stroke-width="1"/><path d="M22 28 q-4.5-5-4.5-8 a4.5 4.5 0 0 1 9 0 q0 3-4.5 8 Z" fill="#fff"/><circle cx="22" cy="20" r="1.6" fill="#6b429c"/></svg>
        <span class="contact-text">Tallow Crest Joinery<br>1187 N Orchard Ln Sample Twp,<br>MI 48211</span>
      </li>
    </ul>

    <div class="social-list">
      <span class="social-dot"></span>
      <span class="social-dot is-hover"></span>
      <span class="social-dot"></span>
    </div>

    <div class="menu-close">
      <svg width="16" height="16" viewBox="0 0 16 16"><path d="M1 1 L15 15 M15 1 L1 15" stroke="#6b429c" stroke-width="1.8"/></svg>
    </div>
  </aside>
</body>
</html>
```